Этикетка для Частная пивоварня " Корвенталь"
Опишите свою организацию или продукт и целевую аудиторию
Завод KORVENTAL построен и введен в эксплуатацию в 2015 году. Мы используем в процессе производства только натуральные ингредиенты высокого качества: немецкий хмель двух сортов и солод.
Целевая аудитория нашего пива- в основной массе мужчины.
Комментарии и пожелания для дизайнеров
Необходимо разработать концепт дизайна этикета на пиво « Тарвинское». Форма самой этикетки не принципиальна: может быть как прямоугольной, так и округлой формы. Главное требование-она должна гармонично сочетаться с формой бутылки.
Цветовая гамма для Тарвинского–готовы рассмотреть варианты: как сине-желто-белая, так и бежевая. Хотелось бы привлечь клиента узнаваемым дизайном пива «Тарвинское», ретро -стиль, но в то же время этикетка должна отличаться от представленных на рынке.
О производителе на этикетке будет говорить лишь фирменный логотип.
Обязательная информация на лицевую часть: « пиво светлое пастеризованное», « настоящее живое», « изготовлено из натуральных ингредиентов».
Контрэтикетка будет содержать текстовую часть( информация о составе, производителе, информацию для потребителя).
Планируем печать на льне. В качестве логотипа используется буква в обрамлении.

```html
<!DOCTYPE html>
<html lang="ru">
<head>
<meta charset="utf-8">
<title>Тарвинское — этикетка</title>
<link href="https://fonts.googleapis.com/css2?family=Oswald:wght@400;500;600&family=Lobster&display=swap" rel="stylesheet">
<style>
  :root {
    --bg: #e2e2e2;
    --label-yellow: #f6ec2c;
    --ink-blue: #1c6f93;
  }
  html, body {
    margin: 0;
    width: 1200px;
    height: 960px;
    overflow: hidden;
    background: var(--bg);
  }
  .stage {
    width: 1200px;
    height: 960px;
    display: flex;
    align-items: center;
    justify-content: center;
  }
  .label { width: 560px; height: 700px; display: block; }
  .label-body { fill: var(--label-yellow); }
  .ink { fill: var(--ink-blue); }
  .ink-line { fill: none; stroke: var(--ink-blue); }
  .meta { font-family: "Oswald", sans-serif; font-weight: 500; font-size: 30px; }
  .meta-unit { font-size: 15px; }
  .arc-text { font-family: "Oswald", sans-serif; font-weight: 400; font-size: 34px; letter-spacing: 5px; }
  .maker { font-family: "Oswald", sans-serif; font-weight: 500; font-size: 22px; letter-spacing: 1px; }
  .product-name {
    font-family: "Lobster", cursive;
    font-size: 88px;
    stroke: var(--label-yellow);
    stroke-width: 10px;
    paint-order: stroke;
  }
  .stars { font-family: "Oswald", sans-serif; font-size: 18px; letter-spacing: 4px; }
  .claim { font-family: "Oswald", sans-serif; font-weight: 600; font-size: 40px; letter-spacing: 1px; }
  .fine { font-family: "Oswald", sans-serif; font-weight: 400; font-size: 16px; letter-spacing: 1px; }
</style>
</head>
<body>
<main class="stage">
  <svg class="label" viewBox="0 0 560 700" xmlns="http://www.w3.org/2000/svg">
    <defs>
      <path id="arc-top" d="M105,340 A175,175 0 0 1 455,340"/>
      <path id="arc-bottom" d="M88,340 A192,192 0 0 0 472,340"/>
    </defs>

    <rect class="label-body" x="0" y="0" width="560" height="700" rx="150" ry="150"/>

    <!-- hop emblem -->
    <circle class="ink-line" cx="280" cy="95" r="44" stroke-width="4"/>
    <circle class="ink" cx="280" cy="97" r="30" role="img" aria-label="Шишка хмеля"/>

    <!-- volume and strength -->
    <text class="meta ink" x="70" y="195">0,5 L</text>
    <text class="meta ink" x="420" y="195">4,9<tspan class="meta-unit" dx="4">ALC</tspan></text>

    <!-- round seal -->
    <circle class="ink-line" cx="280" cy="340" r="150" stroke-width="4"/>
    <text class="arc-text ink" text-anchor="middle">
      <textPath href="#arc-top" startOffset="50%">ПИВО СВЕТЛОЕ</textPath>
    </text>
    <text class="arc-text ink" text-anchor="middle">
      <textPath href="#arc-bottom" startOffset="50%">ПАСТЕРИЗОВАННОЕ</textPath>
    </text>

    <circle class="ink-line" cx="280" cy="262" r="16" stroke-width="3"/>
    <text class="maker ink" x="280" y="312" text-anchor="middle">KORVENTAL</text>
    <text class="product-name ink" x="280" y="385" text-anchor="middle">Тарвинское</text>
    <text class="stars ink" x="282" y="440" text-anchor="middle">★★★★★</text>

    <!-- front claims -->
    <circle class="ink" cx="95" cy="565" r="9" role="img" aria-label="Хмель"/>
    <circle class="ink" cx="465" cy="565" r="9" role="img" aria-label="Хмель"/>
    <text class="claim ink" x="280" y="580" text-anchor="middle">ЖИВОЕ ПИВО</text>
    <text class="fine ink" x="280" y="610" text-anchor="middle">ИЗГОТОВЛЕНО ИЗ НАТУРАЛЬНЫХ</text>
    <text class="fine ink" x="280" y="630" text-anchor="middle">ИНГРЕДИЕНТОВ</text>
  </svg>
</main>
</body>
</html>
```